本当に沢山のデザインをご提案くださいましてありがとうございました。
どのデザインも素晴らしく、社内選考も難航いたしましたが、
kuro.m様のデザインが、今までの弊社にはなかったデザインであったこと。
そして今回の商品が今までとは違った、千葉県産の特産を使用したデザインで
今までの社内とは違った雰囲気を出したかったこと、
何より遠目から見た際に分かりやすく、インパクトのあるデザインだったこと
上記が決め手となり採用いたしました。
本当に多くのデザイナーの皆様にご提案いただけましたこと、
なによりご参加いただけましたこと、本当に感謝してもしきれません。
今回初参加してくだった方のみならず、
いつも弊社のコンペに参加くださっている皆様のお力添えがあり、
新商品を出すことができております。
デザイン性が高いデザインばかりで、
いつも社内選考も大盛り上がりしておりますが、
そうして社内が盛り上がれるのも、参加してくださった皆様のおかげでございます。
この度も誠にありがとうございました。
また、デザインを募集する際には、
お力添えをいただけますと幸いでございます。
この度は、誠にありがとうございました。
【新商品】新商品「メープルアーモンドクリーム(仮)」のラベルデザイン【報酬10万円】 シール・ラベルデザインの仕事の依頼
ご参加くださるクリエイターの皆様へ
お願いといたしまして、
フリー素材の画像やイラストを使用したデザインは
ご遠慮ください。
(パターン・フォントは可)
クリエイターの皆様へ
ご質問の中に、実際のピーナッツバターの色味について
ご質問をいただいておりましたので、
テストでの製品になりますが、
画像を添付いたします。
ぜひ、ご利用いただけますと幸いでございます。
一部不足点がございましたので、再度ご説明いたします。
★フリー素材に関しまして
全追記でお知らせいたしましたフリー素材について補足いたします。
フリー素材に関しましては、「文字」及び「パターン」のみ
フリー素材使用可でお願いいたします。
★瓶のサイズに関しまして
瓶のサイズを明記しておりませんでしたので、明記いたします。
直径:6㎝
高さ:9.5㎝(蓋含む)
何かその他ご質問やご不明点がございましたら、
お気軽にお問合せいただけますと幸いでございます。
何卒よろしくお願い申し上げます。
多くのご提案をいただきまして、
誠にありがとうございます!
裏貼りに関しましてお問合せがございましたので、
こちらに載せさせていただきます。
裏貼りですが、この度デザインをいただいた部分とは別に
裏貼りがございます。
裏貼りに関しましては、底ではなくデザインの背面になります。
それにより、実際は瓶に対して商品の中身が見えるという意味では
20㎝程でございます。
【裏貼りサイズ】
縦650mm
横830mm
製造会社のかたより詳細写真をいただきましたので、
添付いたします。
引き続きよろしくお願いいたします。
この商品を販売するにあたった経緯のご質問が多かったので記載させていただきます。
弊社ではずっと「千葉県産」の何かを使った商品ができないかと考えていました。
千葉県と言えば枇杷がありますが、枇杷と蜂蜜のコラボだと金額がとても高額になり、断念したこともございます。
この度偶然ではありましたが、ピーナッツバターを得意とされる業者さまとお話をする機会がありました。
その際に、ピーナッツバターに砂糖などは使用されているけれども、蜂蜜を砂糖代わりに使用するとどうなんだろう…。
という考えから試作品を作っていただきました。
結果、とても美味しく、これならお客さまにも喜んでいただける!
という味の確信もあり、また念願だった千葉県産の何かを使った弊社オリジナルの商品が作れるという喜びもありました。
このような非常に弊社といたしましては、念願叶う商品であり、
力を入れる商品です。
あまり商品それだけのブースを作ることは少ないですが、
今回はそれだけ力を入れている商品、また念願の商品、ということもあり
専用ブースをつくり、販売するということを決めました。
何か皆様のこの思いや経緯が参考になりましたら、幸いでございます。
クリエイターの皆様
想いとしてもう1つ記載させていただきます。
現在、沢山の商品をお客様にご購入いただいていますが、
「黒糖入り生姜湯」という商品があり、長年売れ筋1位の座から
落ちないぐらい根強い人気があります。
様々な商品を開発し、売り出していますが、これを崩す
第2の看板商品が未だ出てきていません。
その大人気商品を落とすぐらいの売れ筋商品になれる力があると思っています。
この商品が弊社の第2の看板商品になってくれれば、そのような思いでおります。
商品の美味しさだけでは売れません。
そこに皆様のデザインのお力をお借りして、ぜひ弊社の看板商品になることを目指していきたいと思っております。

```html
<!DOCTYPE html>
<html lang="ja">
<head>
<meta charset="utf-8">
<title>メープルアーモンドクリーム ラベルデザイン</title>
<link rel="stylesheet" href="https://fonts.googleapis.com/css2?family=Noto+Sans+JP:wght@400;500&family=Shippori+Mincho:wght@500;700&family=Noto+Serif:wght@400&display=swap">
<style>
  :root {
    --paper: #ffffff;
    --ink: #222222;
    --rule: #333333;
    --cream: #f3dfb8;
    --sand: #e7c48a;
    --honey: #d9a441;
    --caramel: #b87a3a;
    --cocoa: #7a4a2a;
    --label-ink: #4a2e1c;
    --glass: #efe6da;
    --lid: #b58a3c;
  }
  * { margin: 0; padding: 0; box-sizing: border-box; }
  html, body { width: 1200px; height: 848px; overflow: hidden; background: var(--paper); }
  body { position: relative; font-family: "Noto Sans JP", sans-serif; color: var(--ink); }

  .sheet-header {
    position: absolute; left: 56px; right: 56px; top: 40px;
    display: flex; justify-content: space-between; align-items: baseline;
    font-size: 15px; padding-bottom: 10px; border-bottom: 1.5px solid var(--rule);
  }

  .section-title { position: absolute; font-size: 21px; font-weight: 500; }
  .section-title.label-title { left: 124px; top: 244px; }
  .section-title.image-title { left: 750px; top: 166px; }
  .section-title::before { content: "■"; margin-right: 8px; }

  .label {
    position: absolute; left: 124px; top: 306px; width: 522px; height: 238px;
    overflow: hidden;
  }
  .label-pattern {
    position: absolute; inset: 0;
    background:
      radial-gradient(circle at 15% 70%, var(--honey) 0 16%, transparent 17%),
      radial-gradient(circle at 85% 25%, var(--caramel) 0 14%, transparent 15%),
      radial-gradient(circle at 78% 85%, var(--sand) 0 18%, transparent 19%),
      radial-gradient(circle at 25% 15%, var(--caramel) 0 10%, transparent 11%),
      linear-gradient(135deg, var(--cream), var(--sand));
  }
  .label-panel {
    position: absolute; left: 156px; top: 38px; width: 190px; height: 186px;
    background: var(--paper); border: 1px solid var(--sand);
    display: flex; flex-direction: column; align-items: center;
    padding-top: 12px; color: var(--label-ink);
    font-family: "Shippori Mincho", serif;
  }
  .brand { display: flex; align-items: center; gap: 5px; font-size: 10px; font-weight: 700; }
  .brand-dot { width: 18px; height: 18px; border-radius: 50%; background: var(--cocoa); }
  .product-name { margin-top: 12px; font-size: 15px; font-weight: 700; text-align: center; line-height: 1.35; letter-spacing: .04em; }
  .product-name-en { margin-top: 4px; font-family: "Noto Serif", serif; font-size: 9px; letter-spacing: .06em; }
  .product-note { margin-top: 16px; font-size: 8px; text-align: center; line-height: 1.7; }

  .dimension { position: absolute; font-size: 17px; }
  .dimension.label-size { left: 452px; top: 618px; }
  .dimension.jar-size { left: 858px; top: 718px; }

  .jar-visual {
    position: absolute; left: 770px; top: 220px; width: 274px; height: 470px;
    border-radius: 30px 30px 22px 22px;
    background:
      linear-gradient(180deg, var(--lid) 0 14%, var(--glass) 14% 28%, var(--sand) 28% 80%, var(--glass) 80% 100%);
  }
</style>
</head>
<body>
  <header class="sheet-header">
    <span>株式会社花蜜舎 御中 _ メープルアーモンドクリームラベルデザイン</span>
    <span>2024/02/14</span>
  </header>

  <h2 class="section-title label-title">Label</h2>
  <section class="label">
    <div class="label-pattern" role="img" aria-label="蜂の巣模様と丸や縞の抽象パターン(ベージュ・蜂蜜色・茶色)"></div>
    <div class="label-panel">
      <div class="brand"><span class="brand-dot"></span><span>花蜜舎</span></div>
      <p class="product-name">メープル<br>アーモンドクリーム</p>
      <p class="product-name-en">Maple Almond Cream</p>
      <p class="product-note">千葉県産の落花生<br>×<br>花蜜舎の蜂蜜</p>
    </div>
  </section>
  <p class="dimension label-size">H60mm×W110mm</p>

  <h2 class="section-title image-title">Image</h2>
  <div class="jar-visual" role="img" aria-label="金色の蓋の瓶にラベルを巻いた仕上がりイメージ"></div>
  <p class="dimension jar-size">H95mm×W60mm</p>
</body>
</html>
```